Summit Builders Web Site / Business Cards

Construction Company that specializes in Water and Fire Damage, Residential ReModels, Landscaping and Building ADU (Accessory Dwelling Unit)

Growing and changing families often need additional space, and a remodeling project can often provide that. Adding a new area, or repurposing an existing one can satisfy this requirement.

Other times, homeowners want to update the look in their kitchen or bathroom with more than just a change of cabinetry or vanity doors and drawers. Whatever your needs are, Summit Builders has skilled workers who are bonded and insured, and ready to make your dreams and visions a reality.

Target Market(s)

Home Owners

Industry/Entity Type

Construction Company

Contact Information for Business Card

Center Logo with our information on the corners

Back side to be Logo Only
Contact Info
CSLB License # 4829516
info@summitbuildersca.example
www.summitbuildersca.example

Coding

Coded - Design and coding required

Number of Pages Required

5+ page

Font styles to use
Serif
Sans Serif

Requirements
Must have
• Using our Logo Colors
Home
About Us
Services
Projects / Portfolio
Contact Us
Nice to have
• Colors matching our Logo
Should not have
• Black because it doesnt match our logo

```html
<!DOCTYPE html>
<html lang="en">
<head>
<meta charset="utf-8">
<title>Summit Builders</title>
<link href="https://fonts.googleapis.com/css2?family=Poppins:wght@300;400;500;600;700&display=swap" rel="stylesheet">
<style>
:root{
  --orange:#ff6600;
  --slate:#3c3e46;
  --ink:#3a3a3a;
  --muted:#6a6a6a;
  --white:#ffffff;
  --line:#d6d6d6;
}
*{box-sizing:border-box;margin:0;padding:0}
html,body{width:1200px;height:3675px;overflow:hidden;background:var(--white)}
body{font-family:'Poppins',sans-serif;color:var(--ink)}
.canvas{position:relative;width:1200px;height:3675px;overflow:hidden}
.abs{position:absolute}
.center{left:0;width:1200px;text-align:center}

/* header */
.brand{position:absolute;left:172px;top:22px;display:flex;align-items:center;gap:10px}
.brand-square{width:22px;height:22px;background:var(--orange)}
.brand-name{font-size:22px;font-weight:600;color:var(--slate);letter-spacing:1px;line-height:1}
.topbar{position:absolute;top:12px;left:650px;display:flex;gap:28px;font-size:11px;color:var(--slate);align-items:center}
.topbar .item{display:flex;align-items:center;gap:6px}
.social{display:flex;gap:10px;margin-left:0}
.social span{width:13px;height:13px;background:var(--orange);border-radius:2px;display:block}
.nav{position:absolute;top:56px;left:656px;display:flex;gap:27px;font-size:11px;font-weight:500;color:var(--slate)}
.nav .active{color:var(--orange);position:relative}
.nav .active::after{content:"";position:absolute;left:50%;top:24px;width:28px;height:4px;margin-left:-14px;background:var(--orange)}

/* hero */
.hero{position:absolute;top:90px;left:0;width:1200px;height:614px;
  background:linear-gradient(180deg,#5b6a7a 0%,#8a8578 40%,#6b5240 70%,#2e3a28 100%);
  clip-path:polygon(0 0,1200px 0,1200px 459px,600px 614px,0 459px)}
.hero-title{top:262px;font-size:33px;line-height:41px;color:var(--white);font-weight:300;letter-spacing:1px}
.hero-title b{font-weight:700}
.hero-sub{top:342px;font-size:13px;line-height:16px;color:var(--white);font-weight:500}
.btn{position:absolute;background:var(--orange);color:var(--white);font-size:11px;font-weight:500;display:flex;align-items:center;justify-content:center;letter-spacing:.3px}
.dots{display:flex;gap:8px;justify-content:center}
.dots .sq{width:9px;height:9px;border:1.5px solid var(--white)}
.dots .sq.on{background:var(--orange);border-color:var(--orange)}

/* section headings */
.eyebrow{font-size:13px;font-weight:500;color:var(--slate);display:flex;justify-content:center;align-items:center;gap:10px}
.eyebrow::before,.eyebrow::after{content:"";width:36px;height:1px;background:currentColor}
.heading{font-size:24px;font-weight:300;color:var(--slate);letter-spacing:.5px}
.heading b{font-weight:600}
.heading em{font-style:normal;color:var(--orange);font-weight:500}
.light{color:var(--white)}

.about-text{top:832px;left:300px;width:600px;text-align:center;font-size:10.5px;line-height:18px;color:var(--muted)}
.about-photo{position:absolute;left:0;top:780px;width:1200px;height:507px;
  background:linear-gradient(180deg,#c9cfd6 0%,#9a9a8e 45%,#5f7a45 80%,#6d8a4c 100%);
  clip-path:polygon(0 100px,260px 200px,940px 200px,1200px 0,1200px 507px,0 507px)}

/* services */
.services{position:absolute;top:1287px;left:0;width:1200px;height:480px;background:var(--orange)}
.service{position:absolute;top:156px;width:200px;text-align:center}
.service .disc{width:200px;height:200px;border-radius:50%;margin-bottom:22px}
.service p{font-size:16px;font-weight:500;color:var(--white);line-height:20px;letter-spacing:.5px}

/* projects */
.project{position:absolute;top:1916px;width:199px;height:198px}

/* cta */
.cta{position:absolute;top:2255px;left:0;width:1200px;height:449px;
  background:linear-gradient(180deg,#2b3447 0%,#3a3a44 50%,#4a3c30 80%,#2c3328 100%)}
.cta-text{top:2436px;font-size:29px;line-height:32px;font-weight:300;color:var(--white);letter-spacing:.5px}

/* testimonials */
.card{position:absolute;top:2868px;width:262px;height:226px;background:var(--white);box-shadow:0 2px 10px rgba(60,62,70,.12);text-align:center;padding:38px 24px 0}
.quote{position:absolute;top:-12px;left:0;width:100%;text-align:center}
.card h4{font-size:13px;font-weight:600;color:var(--orange);line-height:16px}
.card .role{font-size:11px;color:var(--slate);line-height:14px}
.card .says{margin-top:20px;font-size:9.8px;line-height:18px;color:var(--muted)}
.tdots{display:flex;gap:8px;justify-content:center}
.tdots span{width:7px;height:7px;border-radius:50%;background:#8b8d95}
.tdots span.on{background:var(--orange)}

/* footer */
.footer{position:absolute;top:3180px;left:0;width:1200px;height:495px;background:var(--slate);
  clip-path:polygon(0 156px,600px 0,1200px 156px,1200px 495px,0 495px)}
.foot-brand{top:3262px;display:flex;flex-direction:column;align-items:center;gap:8px}
.foot-brand .brand-name{color:var(--white);font-size:30px;letter-spacing:2px}
.fcol{position:absolute;top:3394px;color:var(--white)}
.fcol h5{font-size:15px;font-weight:400;margin-bottom:12px}
.fcol ul{list-style:none;font-size:10.5px;line-height:21px}
.fcol li::before{content:"\25C6";font-size:6px;margin-right:6px;vertical-align:2px}
.contact-row{display:flex;gap:12px;font-size:10.5px;line-height:19px;margin-bottom:10px}
.contact-row svg{flex:none;margin-top:3px}
.hours{font-size:10.5px;line-height:16px}
.fsocial{display:flex;gap:10px;margin-top:10px}
.fsocial span{width:13px;height:13px;background:var(--white);border-radius:2px}
.rule{position:absolute;top:3620px;left:172px;width:855px;height:1px;background:#5a5c64}
.legal{position:absolute;top:3640px;font-size:10.5px;color:var(--white)}
</style>
</head>
<body>
<div class="canvas">

  <!-- header -->
  <div class="brand"><span class="brand-square"></span><span class="brand-name">SUMMIT BUILDERS</span></div>
  <div class="topbar">
    <span class="item">
      <svg width="11" height="11" viewBox="0 0 24 24"><path fill="#ff6600" d="M6.6 10.8a15 15 0 0 0 6.6 6.6l2.2-2.2c.3-.3.7-.4 1-.2 1.1.4 2.3.6 3.6.6.6 0 1 .4 1 1V20c0 .6-.4 1-1 1A17 17 0 0 1 3 4c0-.6.4-1 1-1h3.5c.6 0 1 .4 1 1 0 1.3.2 2.5.6 3.6.1.3 0 .7-.2 1z"/></svg>
      +1 555 014 2290
    </span>
    <span class="item">
      <svg width="12" height="9" viewBox="0 0 24 18"><rect width="24" height="18" fill="#ff6600"/><path d="M0 0l12 9 12-9" fill="none" stroke="#fff" stroke-width="2"/></svg>
      office@summitbuildersca.example
    </span>
    <span class="social"><span></span><span></span></span>
  </div>
  <nav class="nav">
    <span class="active">HOME</span><span>ABOUT US</span><span>SERVICES</span><span>PROJECTS</span><span>CONTACT US</span>
  </nav>

  <!-- hero -->
  <div class="hero" role="img" aria-label="Modern two-storey house with warm lit windows at dusk"></div>
  <svg class="abs" style="left:138px;top:301px" width="34" height="34" viewBox="0 0 34 34"><rect x="6" y="6" width="22" height="22" transform="rotate(45 17 17)" fill="none" stroke="#fff" stroke-width="1.5"/><path d="M19 12l-5 5 5 5" fill="none" stroke="#fff" stroke-width="1.5"/></svg>
  <svg class="abs" style="left:1027px;top:301px" width="34" height="34" viewBox="0 0 34 34"><rect x="6" y="6" width="22" height="22" transform="rotate(45 17 17)" fill="none" stroke="#fff" stroke-width="1.5"/><path d="M15 12l5 5-5 5" fill="none" stroke="#fff" stroke-width="1.5"/></svg>
  <h1 class="abs center hero-title"><b>QUALITY</b> EXPERTISE<br>CRAFTSMANSHIP <b>RESULTS</b></h1>
  <p class="abs center hero-sub">Specializes in Water and Fire Damage, Residential ReModels,<br>Landscaping and Building ADU (Accessory Dwelling Unit)</p>
  <div class="btn" style="left:532px;top:404px;width:134px;height:40px">EXPLORE MORE</div>
  <div class="abs center dots" style="top:653px"><span class="sq"></span><span class="sq on"></span><span class="sq"></span><span class="sq"></span></div>

  <!-- about -->
  <div class="about-photo" role="img" aria-label="Suburban street of family homes with green lawns"></div>
  <div class="abs center eyebrow" style="top:761px">ABOUT US</div>
  <h2 class="abs center heading" style="top:791px">Welcome To <em>Summit Builders</em></h2>
  <p class="abs about-text">Lorem ipsum dolor sit amet, consectetur adipiscing elit. Sed in libero malesuada, congue nibh sed, dignissim enim. Nam ante leo, sagittis eget tincidunt vitae, consectetur at nibh. Fusce bibendum augue libero. Aenean consequat massa sed suscipit dapibus. Sed fringilla nibh id pharetra tincidunt. Integer vitae sem purus. Morbi in ultricies eros, sit amet tincidunt neque. Pellentesque molestie sagittis augue, eu ultricies lectus.</p>
  <div class="btn" style="left:532px;top:919px;width:134px;height:40px">LEARN MORE</div>

  <!-- services -->
  <section class="services">
    <div class="abs center eyebrow light" style="top:56px">OUR SERVICES</div>
    <h2 class="abs center heading light" style="top:86px">We Tackle All Sorts of jobs, <b>On All Scales</b></h2>
    <div class="service" style="left:172px"><div class="disc" role="img" aria-label="Restored family home" style="background:linear-gradient(180deg,#7b9ac4,#6a6e7a 60%,#4a5a3a)"></div><p>Water and<br>Fire Damage</p></div>
    <div class="service" style="left:390px"><div class="disc" role="img" aria-label="Interior room under remodel" style="background:linear-gradient(90deg,#c89a70,#e4ddd2 55%,#a9b0b6)"></div><p>Residential<br>ReModels</p></div>
    <div class="service" style="left:609px"><div class="disc" role="img" aria-label="Landscaped garden with flower beds" style="background:linear-gradient(180deg,#a7b48a,#4f9a2e 55%,#3c7e22)"></div><p>Landscaping</p></div>
    <div class="service" style="left:826px"><div class="disc" role="img" aria-label="New accessory building exterior" style="background:linear-gradient(180deg,#6d96d0,#e3dccd 55%,#b9b1a3)"></div><p>Building ADU</p></div>
  </section>

  <!-- projects -->
  <div class="abs center eyebrow" style="top:1823px">OUR PROJECTS</div>
  <h2 class="abs center heading" style="top:1852px">Our Recent &amp; <b>Complete Projects</b></h2>
  <div class="project" style="left:172px;background:linear-gradient(180deg,#6d96d0,#e3dccd 50%,#a9a295)" role="img" aria-label="Completed school building"></div>
  <div class="project" style="left:390px;background:linear-gradient(180deg,#7b9ac4,#6a6e7a 55%,#4a4e55)" role="img" aria-label="Completed family house at dusk"></div>
  <div class="project" style="left:609px;background:linear-gradient(180deg,#3f72c4,#b9a89a 55%,#5a7d3a)" role="img" aria-label="Completed two-storey home"></div>
  <div class="project" style="left:827px;background:linear-gradient(180deg,#7ab0e0,#d8c060 45%,#3f8a2a)" role="img" aria-label="Completed villa with landscaped grounds"></div>
  <div class="btn" style="left:532px;top:2153px;width:165px;height:40px">VIEW ALL PROJECTS</div>

  <!-- call to action -->
  <div class="cta" role="img" aria-label="Lit family home at night"></div>
  <div class="abs" style="left:530px;top:2417px;width:140px;height:1.5px;background:var(--white)"></div>
  <p class="abs center cta-text">Summit Builders has skilled workers who are<br>bonded and insured, and ready to make<br>your dreams and visions a reality.</p>
  <div class="btn" style="left:510px;top:2558px;width:180px;height:39px">GET STARTED TODAY!</div>

  <!-- testimonials -->
  <div class="abs center eyebrow" style="top:2761px">TESTIMONIAL</div>
  <h2 class="abs center heading" style="top:2789px">What our <b>Customers</b> are Saying</h2>

  <div class="card" style="left:172px">
    <div class="quote"><svg width="28" height="22" viewBox="0 0 28 22"><path fill="#ff6600" d="M0 0h12v11l-5 11H2l4-10H0zM16 0h12v11l-5 11h-5l4-10h-6z"/></svg></div>
    <h4>John Doe</h4><p class="role">Chairman Orvale</p>
    <p class="says">"...and for all the wonderful work you and your crew are doing. Our team has nothing but good things to say - we are really fortunate to have found you for this project!"</p>
  </div>
  <div class="card" style="left:469px">
    <div class="quote"><svg width="28" height="22" viewBox="0 0 28 22"><path fill="#ff6600" d="M0 0h12v11l-5 11H2l4-10H0zM16 0h12v11l-5 11h-5l4-10h-6z"/></svg></div>
    <h4>Elena Marsh</h4><p class="role">Project Manager</p>
    <p class="says">Summit Builders is one of the best general contractors we've worked with. The entire team tactfully delivered a project of exceptional quality while staying on schedule and under budget. We hope to work with Summit again in the near future!"</p>
  </div>
  <div class="card" style="left:765px">
    <div class="quote"><svg width="28" height="22" viewBox="0 0 28 22"><path fill="#ff6600" d="M0 0h12v11l-5 11H2l4-10H0zM16 0h12v11l-5 11h-5l4-10h-6z"/></svg></div>
    <h4>John Doe</h4><p class="role">Chairman Orvale</p>
    <p class="says">"...and for all the wonderful work you and your crew are doing. Our team has nothing but good things to say - we are really fortunate to have found you for this project!"</p>
  </div>
  <div class="abs center tdots" style="top:3125px"><span class="on"></span><span></span><span></span><span></span></div>

  <!-- footer -->
  <footer class="footer"></footer>
  <div class="abs center foot-brand"><span class="brand-square" style="width:26px;height:26px"></span><span class="brand-name">SUMMIT BUILDERS</span></div>

  <div class="fcol" style="left:172px">
    <h5>Quick Links</h5>
    <ul><li>Home</li><li>About Us</li><li>Services</li><li>Projects</li><li>Contact Us</li></ul>
  </div>
  <div class="fcol" style="left:330px">
    <h5>Our Services</h5>
    <ul><li>Water and Fire Damage</li><li>Residential ReModels</li><li>Landscaping</li><li>Building ADU</li></ul>
  </div>
  <div class="fcol" style="left:559px;width:230px">
    <h5>Quick Contact</h5>
    <div class="contact-row"><svg width="10" height="14" viewBox="0 0 10 14"><path fill="#fff" d="M5 0a5 5 0 0 1 5 5c0 4-5 9-5 9S0 9 0 5a5 5 0 0 1 5-5zm0 3a2 2 0 1 0 0 4 2 2 0 0 0 0-4z"/></svg><span>Daniel R Hale | Branch Manager<br>412 W Cedar Ridge Rd Fairview,<br>CA 90000</span></div>
    <div class="contact-row"><svg width="11" height="11" viewBox="0 0 24 24"><path fill="#fff" d="M6.6 10.8a15 15 0 0 0 6.6 6.6l2.2-2.2c.3-.3.7-.4 1-.2 1.1.4 2.3.6 3.6.6.6 0 1 .4 1 1V20c0 .6-.4 1-1 1A17 17 0 0 1 3 4c0-.6.4-1 1-1h3.5c.6 0 1 .4 1 1 0 1.3.2 2.5.6 3.6.1.3 0 .7-.2 1z"/></svg><span>555-014-2290, 555-018-3374</span></div>
    <div class="contact-row"><svg width="11" height="11" viewBox="0 0 12 12"><rect x="2" y="0" width="8" height="4" fill="none" stroke="#fff"/><rect x="0" y="4" width="12" height="6" fill="#fff"/><rect x="3" y="8" width="6" height="4" fill="#fff" stroke="#3c3e46"/></svg><span>555-016-7731</span></div>
    <div class="contact-row"><svg width="12" height="9" viewBox="0 0 24 18"><rect width="24" height="18" fill="#fff"/><path d="M0 0l12 9 12-9" fill="none" stroke="#3c3e46" stroke-width="2"/></svg><span>office@summitbuildersca.example</span></div>
  </div>
  <div class="fcol" style="left:836px;width:200px">
    <h5>Business Hours</h5>
    <p class="hours">Mon - Fri : 10:00 – 16:00<br>saturday : 12:00 – 15:00<br>sunday and holidays : 09:00 – 12:00</p>
    <h5 style="margin-top:26px;margin-bottom:6px">Our Social Media!</h5>
    <p class="hours">Follow and get to know us!</p>
    <div class="fsocial"><span></span><span></span></div>
  </div>

  <div class="rule"></div>
  <p class="legal" style="left:172px">Copyright © 2020 Summit Builders | All Rights Reserved.</p>
  <p class="legal" style="right:173px">Privacy Policy | Terms &amp; Conditions</p>
</div>
</body>
</html>
```